Life Coach for Lawyers Business Card Design

Elegant, original, business card design for life coaching service for associate attorneys who work in big law and struggle with stress, overwhelm, and time management. Double sided design.

Target Market(s)

Women associate attorneys who work in big law and struggle with stress, overwhelm, and time management.

Industry/Entity Type

Life Coaching

Contact Information for Business Card

Marissa Pendrell
Life Coach
518.677.3941
calmbriefcounsel.net
marissa@calmbriefcounsel.net
@calmbriefcounsel (Instagram)

Font styles to use
Other font styles liked:
• Silver South font duo. See uploaded files.

Requirements
Must have
• Icons for phone, website, email, and Instagram instead of words. Specific colors used in my logo (171B2B, 421121, FFFFFF)
Nice to have
• Foil. Embossed. Feminine design.
Should not have
• Any colors other than those used in logo. See uploaded files.

```html
<!DOCTYPE html>
<html lang="en">
<head>
<meta charset="utf-8">
<title>Calm Brief Counsel – Business Card</title>
<link href="https://fonts.googleapis.com/css2?family=Roboto:wght@400;500&display=swap" rel="stylesheet">
<style>
  :root {
    --stage: #1c1d22;
    --wine: #421121;
    --wine-light: #5a1f33;
    --wine-dark: #36101b;
    --silver: #ece8ea;
    --silver-soft: #c9bcc1;
    --emboss: #6a3447;
  }
  * { margin: 0; padding: 0; box-sizing: border-box; }
  html, body { width: 1200px; height: 900px; overflow: hidden; }
  body {
    background: var(--stage);
    font-family: "Roboto", sans-serif;
    display: flex;
    flex-direction: column;
    align-items: center;
    justify-content: center;
    gap: 40px;
  }
  .card {
    width: 700px;
    height: 400px;
    background: linear-gradient(135deg, var(--wine-dark) 0%, var(--wine) 55%, var(--wine-light) 100%);
    position: relative;
  }
  /* Front */
  .card--front { display: flex; align-items: center; justify-content: center; }
  .front-mark { display: flex; align-items: center; gap: 16px; }
  .front-mark__dot {
    width: 18px; height: 18px; border-radius: 50%;
    background: var(--silver);
  }
  .front-mark__name {
    font-size: 30px; font-weight: 400; letter-spacing: 3px;
    color: var(--silver); text-transform: uppercase;
  }
  /* Back */
  .card--back { display: flex; align-items: center; }
  .back-brand {
    width: 320px; padding-left: 40px;
    font-size: 40px; font-weight: 400; line-height: 1.1;
    letter-spacing: 2px; color: var(--emboss); text-transform: uppercase;
  }
  .back-divider {
    width: 1px; height: 190px; background: var(--silver-soft); opacity: .7;
  }
  .back-details { padding-left: 22px; color: var(--silver); }
  .person-name { font-size: 26px; font-weight: 500; letter-spacing: 1.5px; text-transform: uppercase; }
  .person-role { font-size: 15px; color: var(--silver-soft); margin: 4px 0 22px; letter-spacing: .5px; }
  .contact-list { list-style: none; font-size: 16px; letter-spacing: .5px; }
  .contact-list li { display: flex; align-items: center; gap: 10px; line-height: 1.75; }
  .contact-icon { width: 13px; height: 13px; flex: none; }
</style>
</head>
<body>
  <section class="card card--front">
    <div class="front-mark">
      <span class="front-mark__dot"></span>
      <span class="front-mark__name">Calm Brief Counsel</span>
    </div>
  </section>

  <section class="card card--back">
    <div class="back-brand">Calm Brief Counsel</div>
    <div class="back-divider"></div>
    <div class="back-details">
      <h1 class="person-name">Marissa Pendrell</h1>
      <p class="person-role">Life Coach</p>
      <ul class="contact-list">
        <li>
          <svg class="contact-icon" viewBox="0 0 24 24" fill="var(--silver)" aria-label="Phone"><path d="M6.6 10.8a15.1 15.1 0 0 0 6.6 6.6l2.2-2.2a1 1 0 0 1 1-.25 11.4 11.4 0 0 0 3.6.57 1 1 0 0 1 1 1V20a1 1 0 0 1-1 1A17 17 0 0 1 3 4a1 1 0 0 1 1-1h3.5a1 1 0 0 1 1 1c0 1.25.2 2.45.57 3.57a1 1 0 0 1-.25 1z"/></svg>
          518.677.3941
        </li>
        <li>
          <svg class="contact-icon" viewBox="0 0 24 24" fill="none" stroke="var(--silver)" stroke-width="2" aria-label="Email"><rect x="3" y="5" width="18" height="14"/><path d="M3 6l9 7 9-7"/></svg>
          marissa@calmbriefcounsel.net
        </li>
        <li>
          <svg class="contact-icon" viewBox="0 0 24 24" fill="none" stroke="var(--silver)" stroke-width="2" aria-label="Website"><circle cx="12" cy="12" r="9"/><path d="M3 12h18M12 3c3 3 3 15 0 18M12 3c-3 3-3 15 0 18"/></svg>
          calmbriefcounsel.net
        </li>
        <li>
          <svg class="contact-icon" viewBox="0 0 24 24" fill="none" stroke="var(--silver)" stroke-width="2" aria-label="Social handle"><rect x="4" y="4" width="16" height="16"/></svg>
          @calmbriefcounsel
        </li>
      </ul>
    </div>
  </section>
</body>
</html>
```